Tamsin's Crest CBD Packaging and Branding

We are looking for packaging designs for a new doctor focused CBD brand that is disease specific formulations (i.e. Bone and Joint Formula, Pelvic Formula, Pain Formula, Inflammation Formula, ect.) We would like the first packaging prototype to be our Pain Formulation. Our tagline is, "The Tamsin's Crest" & we would also like the phrase, "Life. Balanced." - We are looking for our Logo to be on the box as well. We currently need a logo as well. We would like the letters "KT" to be more prominent than "nuvo" Our first product will be SoftGels and the active ingredient list can be made up at the moment. Our brand and packaging needs to convey authority, trust and scientific knowledge (since all of our formulations are created by researched and renowned doctors and scientists), but we also don't want to be too clinical feeling, so adding a modern touch. Attached are some sample designs for reference (none are the final iteration) as well as some vectorized art.

Target Market(s)

40-60 year old patients

Industry/Entity Type

Medical And Science

Logo Text

KT Nuvo

Requirements
Must have
• Clean, professional and trusting medical designs with a modern touch. New logo incorporated into the design.
Should not have
• Not too clinical feeling - Not pharmaceutical

```html
<!DOCTYPE html>
<html lang="en">
<head>
<meta charset="utf-8">
<title>KT Nuvo – Joint and Nerve Pain Formula</title>
<link rel="stylesheet" href="https://fonts.googleapis.com/css2?family=Montserrat:wght@300;400&family=Playfair+Display:wght@400&family=Cormorant+Garamond:wght@500&display=swap">
<style>
  :root {
    --backdrop: #8cbacb;
    --panel: #f4f4f4;
    --teal: #3f9f9c;
    --teal-light: #8fe6dc;
    --purple: #7f78b8;
    --violet: #9b6fc6;
    --indigo: #5b5a9c;
    --coral: #e08868;
    --magenta: #a8457e;
    --ink-grey: #6b6b6b;
    --white: #ffffff;
  }
  html, body {
    margin: 0;
    padding: 0;
    width: 1200px;
    height: 789px;
    overflow: hidden;
    background: var(--backdrop);
  }
  .canvas {
    position: relative;
    width: 1200px;
    height: 789px;
    display: flex;
    align-items: center;
    justify-content: center;
  }
  .box-front {
    position: relative;
    width: 470px;
    height: 705px;
    background: var(--panel);
    overflow: hidden;
    box-shadow: 0 10px 30px rgba(40, 70, 90, 0.25);
  }
  .brand-band {
    position: absolute;
    left: 0;
    top: 0;
    width: 100%;
    height: 170px;
    background: linear-gradient(105deg, var(--teal) 0%, var(--indigo) 35%, var(--purple) 60%, var(--purple) 75%, var(--teal) 100%);
  }
  .footer-strip {
    position: absolute;
    left: 0;
    bottom: 0;
    width: 100%;
    height: 40px;
    background: linear-gradient(90deg, var(--teal) 0%, var(--purple) 30%, var(--teal) 65%, var(--violet) 100%);
  }
  .figure-art {
    position: absolute;
    left: 22px;
    top: 90px;
    width: 220px;
    height: 560px;
  }
  .logo {
    position: absolute;
    right: 20px;
    top: 58px;
    text-align: right;
    color: var(--white);
  }
  .logo-name {
    font-family: "Playfair Display", serif;
    font-weight: 400;
    font-size: 46px;
    line-height: 1;
    margin: 0;
  }
  .logo-tagline {
    font-family: "Cormorant Garamond", serif;
    font-weight: 500;
    font-size: 18px;
    line-height: 1.2;
    color: var(--teal-light);
    margin: 8px 0 0;
  }
  .product-copy {
    position: absolute;
    left: 262px;
    top: 440px;
    font-family: "Montserrat", sans-serif;
  }
  .slogan {
    color: var(--teal);
    font-weight: 300;
    font-size: 26px;
    line-height: 1.2;
    margin: 0 0 20px;
  }
  .product-name {
    color: var(--coral);
    font-weight: 300;
    font-size: 20px;
    line-height: 1.25;
    margin: 0;
    white-space: nowrap;
  }
  .dose-form {
    color: var(--ink-grey);
    font-weight: 300;
    font-size: 16px;
    margin: 6px 0 0 44px;
  }
  .count {
    color: var(--ink-grey);
    font-weight: 300;
    font-size: 12px;
    margin: 6px 0 0 20px;
  }
</style>
</head>
<body>
  <main class="canvas">
    <section class="box-front">
      <div class="brand-band"></div>
      <div class="footer-strip"></div>

      <svg class="figure-art" role="img" aria-label="Colourful anatomical illustration of a standing human figure showing muscles and joints" viewBox="0 0 220 560">
        <defs>
          <linearGradient id="figure-tone" x1="0" y1="0" x2="0.4" y2="1">
            <stop offset="0" stop-color="#e08868"/>
            <stop offset="0.45" stop-color="#8e6aa0"/>
            <stop offset="0.8" stop-color="#a8457e"/>
            <stop offset="1" stop-color="#6f73c0"/>
          </linearGradient>
        </defs>
        <rect x="0" y="0" width="220" height="560" rx="26" fill="url(#figure-tone)"/>
      </svg>

      <div class="logo">
        <p class="logo-name">KT Nuvo</p>
        <p class="logo-tagline">The Tamsin's Crest</p>
      </div>

      <div class="product-copy">
        <p class="slogan">Life.<br>Balanced.</p>
        <p class="product-name">Joint and Nerve<br>Pain Formula</p>
        <p class="dose-form">SoftGels</p>
        <p class="count">30 Count</p>
      </div>
    </section>
  </main>
</body>
</html>
```